Process Roadmap for Interior Design Firm

We are looking to ramp up the design appeal of our current process roadmap to be very visually interesting, while staying informative and descriptive about our process.

Target Market(s)

In-house Clients

Industry/Entity Type

Interior Design Firm focused on sustainable and holistic design.

Other font styles liked:
• raleway

Requirements
Must have
• 1.) it would be nice if the graphic provided a more clear indication of the “journey” from one step to the next, so that there was a clear sense of the progression (such that we are directing the viewer) 2.). We would want it to fit on an 8.5”x11” page (the page could be horizontal when we have the Steady Pathway formatted out with the testimonials) (in addition to the testimonials, we may also want to have the detailed descriptions of each step of the process presented below the graphic, so that the graphic is cleaner) 3.) ideally the graphic is clear and simple enough to also be used on our Bi-Weekly Client Updates, which will be typed updates for clients re their project budgets, schedule and scope. The Steady Pathway graphic (without all the testimonials) would be at the end of the update, and would fit on the page horizontally at the bottom, perhaps in a space which is 7.5”w x 4”h or so.
Should not have
• bold or bright colors. Natural neutrals are preferred, such as the ones featured on the provided graphic.

```html
<!DOCTYPE html>
<html lang="en">
<head>
<meta charset="utf-8">
<title>Steady Pathway</title>
<link href="https://fonts.googleapis.com/css2?family=Raleway:wght@300;400;700&display=swap" rel="stylesheet">
<style>
:root{
  --gold:#c39a4f;
  --text-gold:#c6a460;
  --tone-1:#b9ab85;
  --tone-2:#dcd0a7;
  --tone-3:#e5deb8;
  --tone-4:#ebe3d3;
  --paper:#ffffff;
}
*{margin:0;padding:0;box-sizing:border-box}
html,body{width:1200px;height:927px;overflow:hidden;background:var(--paper)}
.page{position:relative;width:1200px;height:927px;font-family:'Raleway',sans-serif}
.brand{position:absolute;left:24px;top:22px;display:flex;align-items:flex-start;gap:14px}
.brand-mark{width:34px;height:34px;border:2px solid var(--gold);margin-top:4px}
.brand-name{color:var(--gold);font-weight:400;font-size:26px;letter-spacing:5px;line-height:32px}
.brand-name span{display:block}
.brand-name .sub{font-size:18px;letter-spacing:6px;text-align:right}
.title{position:absolute;right:72px;top:52px;color:var(--gold);font-weight:700;font-size:57px;letter-spacing:-0.5px}
.roadmap{position:absolute;left:0;top:0}
.step-label{font-family:'Raleway',sans-serif;font-weight:700;font-size:21px;fill:#fff}
.step-col{position:absolute;top:389px;height:343px;border-left:2px dashed var(--tone-1);padding-left:9px;padding-top:13px;width:140px}
.step-col p{color:var(--text-gold);font-weight:300;font-size:16.5px;line-height:23.9px;white-space:nowrap}
.c1{left:90px}.c2{left:238px}
.c3{left:386px;border-color:var(--tone-2)}.c4{left:534px;border-color:var(--tone-2)}
.c5{left:682px;border-color:var(--tone-3)}.c6{left:830px;border-color:var(--tone-3)}
.c7{left:978px;border-color:var(--tone-4)}
</style>
</head>
<body>
<div class="page">
  <div class="brand">
    <div class="brand-mark"></div>
    <div class="brand-name"><span>ALDER HOLT</span><span class="sub">DESIGN</span></div>
  </div>
  <h1 class="title">Steady pathway</h1>

  <svg class="roadmap" width="1200" height="400" viewBox="0 0 1200 400">
    <g class="chevrons">
      <path fill="var(--tone-1)" d="M76 323h140l15 25-15 25H76l15-25z"/>
      <path fill="var(--tone-1)" d="M224 323h140l15 25-15 25H224l15-25z"/>
      <path fill="var(--tone-2)" d="M372 323h140l15 25-15 25H372l15-25z"/>
      <path fill="var(--tone-2)" d="M520 323h140l15 25-15 25H520l15-25z"/>
      <path fill="var(--tone-3)" d="M668 323h140l15 25-15 25H668l15-25z"/>
      <path fill="var(--tone-3)" d="M816 323h140l15 25-15 25H816l15-25z"/>
      <path fill="var(--tone-4)" d="M964 323h140l15 25-15 25H964l15-25z"/>
    </g>
    <g class="badges" stroke="#fff" stroke-width="4">
      <circle cx="148" cy="291" r="38" fill="var(--tone-1)"/>
      <circle cx="296" cy="291" r="38" fill="var(--tone-1)"/>
      <circle cx="444" cy="291" r="38" fill="var(--tone-2)"/>
      <circle cx="592" cy="291" r="38" fill="var(--tone-2)"/>
      <circle cx="740" cy="291" r="38" fill="var(--tone-3)"/>
      <circle cx="888" cy="291" r="38" fill="var(--tone-3)"/>
      <circle cx="1036" cy="291" r="38" fill="var(--tone-4)"/>
    </g>
    <g class="icons" fill="none" stroke="#fff" stroke-width="2" stroke-linecap="round" stroke-linejoin="round">
      <path d="M140 310c-4 0-5-5-2-8 3-4 2-8 0-12-4-6 0-16 10-16 8 0 13 6 13 13 0 8-7 10-8 16-1 5-4 7-8 7"/>
      <path d="M146 290c0-4 3-6 5-6s4 2 4 5"/>
      <path d="M280 291c6-8 26-8 32 0-6 8-26 8-32 0z"/><circle cx="296" cy="291" r="5"/>
      <path d="M296 271v5M281 277l3 3M311 277l-3 3M296 306v5M281 305l3-3M311 305l-3-3"/>
      <rect x="431" y="275" width="26" height="34" rx="1"/><rect x="438" y="271" width="12" height="6"/>
      <path d="M437 286l4 4M441 286l-4 4M448 300l4 4M452 300l-4 4M440 298c4 0 6-3 8-8"/>
      <circle cx="585" cy="279" r="5"/><path d="M583 286h4M575 296h14v10h-14zM600 300l10-12 4 3-10 12-5 1z"/>
      <circle cx="732" cy="280" r="4"/><circle cx="740" cy="278" r="4"/><circle cx="748" cy="280" r="4"/>
      <path d="M724 296c0-6 4-9 8-9M756 296c0-6-4-9-8-9M734 292c0-4 3-6 6-6s6 2 6 6"/>
      <path d="M724 300a16 10 0 0 0 32 0"/>
      <path d="M876 305l22-22M893 276a6 6 0 0 0 8 8l-3-3v-3h3zM879 302l-4 4"/>
      <rect x="1023" y="278" width="24" height="30" rx="2"/>
      <path d="M1028 286h2M1034 286h9M1028 293h2M1034 293h9M1028 300h2M1034 300h9"/>
      <circle cx="1049" cy="277" r="8" fill="var(--tone-4)"/><path d="M1045 277l3 3 5-6"/>
    </g>
    <g class="labels" text-anchor="middle">
      <text class="step-label" x="153" y="356">Listening</text>
      <text class="step-label" x="301" y="356">Visioning</text>
      <text class="step-label" x="449" y="356">Planning</text>
      <text class="step-label" x="597" y="356">Designing</text>
      <text class="step-label" x="745" y="356">Managing</text>
      <text class="step-label" x="893" y="356">Installing</text>
      <text class="step-label" x="1042" y="356">Completing</text>
    </g>
  </svg>

  <div class="step-col c1"><p>Listening to our<br>clients, their<br>land and their<br>home.<br>Identifying their<br>needs,<br>challenges,<br>wishes and<br>dreams.</p></div>
  <div class="step-col c2"><p>Facilitating a<br>guided visioning<br>process to<br>clarify the<br>deepest<br>intention, true<br>purpose and<br>highest<br>potential for<br>their home and<br>their future<br>within it.</p></div>
  <div class="step-col c3"><p>Turning our<br>client’s vision<br>into a clearly<br>defined scope,<br>budget and<br>timeline.<br>Mapping out<br>the steps for<br>making their<br>dream a reality.<br>Setting a<br>meeting<br>schedule from<br>start to finish.</p></div>
  <div class="step-col c4"><p>Following the<br>schedule<br>through the<br>design phases<br>from initial<br>design<br>concepts,<br>technical<br>drawings and<br>details and the<br>selection of all<br>finishes, fixtures<br>and furnishings.</p></div>
  <div class="step-col c5"><p>Co-ordinating<br>with clients,<br>builders,<br>architects and<br>vendors to<br>ensure that the<br>design is<br>executed with<br>excellence and<br>the construction<br>and furnishings<br>are on-time and<br>on-budget.</p></div>
  <div class="step-col c6"><p>Overseeing the<br>inspection,<br>installation and<br>arrangement of<br>all furnishings,<br>lighting, artwork<br>and decorative<br>items.<br>Taking care of<br>every last detail.</p></div>
  <div class="step-col c7"><p>Fixing any<br>issues or<br>defects.<br>Follow up on<br>all remaining<br>items.<br>Completing the<br>final finishing<br>touches to our<br>clients full and<br>total<br>satisfaction.</p></div>
</div>
</body>
</html>
```